Medical Waste Company with Logo

Need a business card design that targets office managers in the medical community. This card will be the front line for our sales team to market our services to the community. We would like to have email, phone number, website. Please use the logo attached to create a design that we would be proud of.

Target Market(s)

Medical Clients

Industry/Entity Type

Medical Supply

Contact Information for Business Card

Please use logo attached

Colors

Designer to choose colors to be used in the design.

Requirements
Must have
• Our logo (see attached file)
Nice to have
• Maybe a pop of some sort, raised..?

```html
<!DOCTYPE html>
<html lang="en">
<head>
<meta charset="utf-8">
<title>Glacier Medical Waste – Business Card</title>
<link rel="stylesheet" href="https://fonts.googleapis.com/css2?family=Montserrat:wght@600&family=Roboto:wght@400;500&family=Open+Sans:wght@400;700&display=swap">
<style>
  :root {
    --backdrop: #c8d1d9;
    --card-light: #e2e8ee;
    --card-edge: #f1f4f7;
    --band-dark: #565859;
    --brand-blue: #1f6aa5;
    --text-white: #ffffff;
    --text-soft: #e6e6e6;
    --divider: #d9d9d9;
    --icon-ink: #565859;
  }
  * { margin: 0; padding: 0; box-sizing: border-box; }
  html, body {
    width: 1200px; height: 1042px; overflow: hidden;
    background: var(--backdrop);
  }
  .business-card {
    position: absolute; left: 120px; top: 213px;
    width: 960px; height: 615px;
    border-radius: 30px; overflow: hidden;
    background: var(--card-light);
    border: 2px solid var(--card-edge);
    box-shadow: 0 14px 40px rgba(40, 60, 80, 0.18);
  }
  .brand-block {
    position: absolute; left: 0; top: 0; width: 100%; height: 352px;
    display: flex; align-items: center; justify-content: center; gap: 22px;
    padding-top: 80px;
  }
  .brand-square {
    width: 30px; height: 30px; background: var(--brand-blue);
  }
  .brand-name {
    font-family: "Montserrat", sans-serif; font-weight: 600;
    font-size: 46px; letter-spacing: 1px; color: var(--brand-blue);
    text-transform: uppercase; line-height: 1;
  }
  .accent-rule {
    position: absolute; left: 0; top: 352px; width: 100%; height: 10px;
    background: var(--brand-blue);
  }
  .contact-band {
    position: absolute; left: 0; top: 362px; width: 100%; height: 253px;
    background: var(--band-dark);
  }
  .person {
    position: absolute; right: calc(960px - 428px); top: 420px; text-align: right;
  }
  .person-name {
    font-family: "Open Sans", sans-serif; font-weight: 700;
    font-size: 28px; color: var(--text-white); line-height: 1.2;
  }
  .person-title {
    font-family: "Roboto", sans-serif; font-weight: 400;
    font-size: 17px; color: var(--text-soft); margin-top: 10px;
    text-transform: uppercase;
  }
  .band-divider {
    position: absolute; left: 486px; top: 379px; width: 2px; height: 183px;
    background: var(--divider);
  }
  .contact-list { list-style: none; position: absolute; left: 528px; top: 394px; }
  .contact-item {
    display: flex; align-items: center; height: 37px;
    font-family: "Roboto", sans-serif; font-size: 21px; color: var(--text-white);
  }
  .contact-icon { width: 26px; height: 26px; margin-right: 7px; flex: none; }
  .contact-item.continued { padding-left: 33px; }
</style>
</head>
<body>
  <article class="business-card">
    <header class="brand-block">
      <span class="brand-square"></span>
      <span class="brand-name">Glacier Medical Waste</span>
    </header>
    <div class="accent-rule"></div>
    <section class="contact-band"></section>

    <div class="person">
      <p class="person-name">Dana Whitfield</p>
      <p class="person-title">Manager</p>
    </div>
    <div class="band-divider"></div>

    <ul class="contact-list">
      <li class="contact-item">
        <svg class="contact-icon" viewBox="0 0 26 26" aria-hidden="true">
          <circle cx="13" cy="13" r="13" fill="#fff"/>
          <path d="M9 6.5c1-.6 1.7 0 2.2 1l1 2.2c.3.8-.2 1.3-.8 1.8-.4.3-.3.8 0 1.3.8 1.3 1.6 2.2 2.8 2.9.5.3.9.3 1.2-.1.6-.6 1.1-1 1.9-.6l2 1.2c.8.5 1 1.3.3 2.1-1 1.2-2.5 1.5-4 .9-3.4-1.5-5.7-4-7-7.3-.5-1.6-.2-3.3 1.4-4.4z" fill="var(--icon-ink)"/>
        </svg>
        206-555-0147
      </li>
      <li class="contact-item">
        <svg class="contact-icon" viewBox="0 0 26 26" aria-hidden="true">
          <circle cx="13" cy="13" r="13" fill="#fff"/>
          <rect x="6.5" y="8.5" width="13" height="9" rx="1.5" fill="var(--icon-ink)"/>
          <path d="M7 9.5l6 4.5 6-4.5" fill="none" stroke="#fff" stroke-width="1.3"/>
        </svg>
        dana@glaciermedwaste.com
      </li>
      <li class="contact-item">
        <svg class="contact-icon" viewBox="0 0 26 26" aria-hidden="true">
          <circle cx="13" cy="13" r="13" fill="#fff"/>
          <g fill="none" stroke="var(--icon-ink)" stroke-width="1.3">
            <circle cx="13" cy="13" r="6.5"/>
            <ellipse cx="13" cy="13" rx="2.8" ry="6.5"/>
            <path d="M6.5 13h13M7.5 9.7h11M7.5 16.3h11"/>
          </g>
        </svg>
        www.glaciermedwaste.com
      </li>
      <li class="contact-item">
        <svg class="contact-icon" viewBox="0 0 26 26" aria-hidden="true">
          <circle cx="13" cy="13" r="13" fill="#fff"/>
          <path d="M13 5.5a5 5 0 0 0-5 5c0 3.8 5 9.5 5 9.5s5-5.7 5-9.5a5 5 0 0 0-5-5z" fill="var(--icon-ink)"/>
          <circle cx="13" cy="10.5" r="2" fill="#fff"/>
        </svg>
        418 Harbor Lane NE
      </li>
      <li class="contact-item continued">Kenmore WA 98028</li>
    </ul>
  </article>
</body>
</html>
```